GUARANTEED! Simple website for independent event planner and consultant...

I need a website that is no more than 5 or 6 pages to illustrate who I am and what I can offer to groups who book hotels for meetings and conferences. I have 20 years of experience planning meetings within hotels and I am now ready to go out on my own and help clients choose venues, negotiate contracts and plan effective meetings. I will focus on clients planning meetings in the mountains of Colorado but I am willing to travel as well. I want to work with a person who is collaborative and can direct me on what they need to move the project along quickly. I already have my logo, a hosting site and work e-mail address. Also, I recently hired a photographer to do head shots. Lastly, it important for me to be able to talk on the phone or skype with this person, as needed and I must be able to make changes to my site down the road when necessary...

Target Market(s)

Corporate Groups

Industry/Entity Type

Event Planning

Coding

Coded - Design and coding required

Number of Pages Required

5+ page

Font styles to use
Sans Serif

Requirements
Must have
• About me page, event planning services offered page, task force and consulting work page, testimonials page, page for blogs, page to contact me/request a proposal. May need advice on what else I need...
Nice to have
• I want it to look sharp and professional. I want people to look at my site and know immediately that they can trust me and the work I can do.
• I don't want it to look like it is over the top as I am not a HUGE company but I do want it to be professional and easy to view and navigate.
Should not have
• Bright colors
• My logo is bright orange and black. I have also used dark grey and orange. See below:
• Orange:
• C = 0
• M = 64
• Y = 100
• K = 0
• Gray:
• C = 67
• M = 60
• Y = 59
• K = 45
• Font: Gotham Book and Gotham Bold

```html
<!DOCTYPE html>
<html lang="en">
<head>
<meta charset="utf-8">
<title>Harlow Event Management</title>
<link href="https://fonts.googleapis.com/css2?family=Raleway:wght@500;600;700&family=Jost:wght@400;500;600&display=swap" rel="stylesheet">
<style>
:root{
  --orange:#f07a1a;
  --orange-dark:#e06a0c;
  --ink:#1d1d1d;
  --text:#333;
  --muted:#666;
  --grey-band:#ececec;
  --frame:#e2e2e2;
  --footer:#2b2b2b;
  --footer-base:#1f1f1f;
  --white:#fff;
}
*{margin:0;padding:0;box-sizing:border-box}
html,body{width:1200px;height:2980px;overflow:hidden}
body{position:relative;background:var(--white);font-family:"Jost",sans-serif;color:var(--text)}
.abs{position:absolute}

/* Heading with bracket accent */
.title{font-family:"Raleway",sans-serif;font-weight:600;color:var(--ink);position:absolute;white-space:nowrap}
.accent{position:relative;display:inline-block}
.accent::before,.accent::after{content:"";position:absolute;left:-4px;right:-4px;height:12px;border:3px solid var(--orange)}
.accent::before{top:-14px;border-bottom:none}
.accent::after{bottom:-10px;border-top:none}

/* Hero */
.hero{position:absolute;left:0;top:0;width:1200px;height:550px;background:linear-gradient(120deg,#6f6a63 0%,#8d8780 35%,#a29b92 60%,#514c47 100%)}
.sidebar{position:absolute;left:0;top:0;width:204px;height:550px;background:rgba(30,30,30,.72)}
.brand{position:absolute;left:26px;top:50px;color:var(--orange);font-family:"Raleway",sans-serif;font-weight:700;font-size:38px;letter-spacing:1px}
.brand-box{position:absolute;left:26px;top:98px;width:14px;height:14px;background:var(--orange)}
.nav{position:absolute;left:0;top:182px;width:204px;list-style:none;text-align:center}
.nav li{font-size:12.5px;color:var(--white);height:36px;line-height:24px}
.nav li.active{color:var(--orange)}
.hero-title{position:absolute;left:400px;top:218px;width:610px;text-align:center;color:var(--white);font-family:"Raleway",sans-serif;font-weight:600;font-size:36px;line-height:56px;text-shadow:0 1px 3px rgba(0,0,0,.3)}

/* About */
.about-text{position:absolute;left:164px;top:692px;width:566px;font-size:13px;line-height:17.5px;color:#222}
.about-text p+p{margin-top:17px}
.btn{position:absolute;background:var(--orange);color:var(--white);font-size:13px;text-align:center;border-radius:2px;border-bottom:3px solid var(--orange-dark)}
.portrait-frame{position:absolute;left:748px;top:610px;width:296px;height:360px;background:var(--frame)}
.portrait{position:absolute;left:12px;top:12px;width:272px;height:336px;background:linear-gradient(160deg,#9a9a9a,#4a4a4a 70%,#2e2e2e)}

/* Services */
.services{position:absolute;left:0;top:1030px;width:1200px;height:510px;background:linear-gradient(180deg,#4e5257 0%,#2f3236 55%,#1a1b1d 100%)}
.service{position:absolute;top:210px;width:200px;text-align:center}
.service .ring{width:114px;height:114px;margin:0 auto;border-radius:50%;background:#dcdcdc;display:flex;align-items:center;justify-content:center}
.service .disc{width:92px;height:92px;border-radius:50%;background:var(--white);display:flex;align-items:center;justify-content:center}
.service .label{margin-top:14px;font-size:14px;font-weight:600;color:var(--white);line-height:18px}
.service.active .label{color:var(--orange)}

/* Gallery */
.tile{position:absolute;background:var(--frame)}
.tile .ph{position:absolute;left:12px;top:12px;right:12px;bottom:12px}

/* Testimonials & blog */
.band{position:absolute;left:0;top:2250px;width:1200px;height:425px;background:var(--grey-band)}
.arrows{position:absolute;display:flex;gap:6px}
.arrows span{width:16px;height:16px;border-radius:50%;border:1.5px solid #777;display:flex;align-items:center;justify-content:center}
.arrows span.on{border-color:var(--orange)}
.quote-box{position:absolute;left:162px;top:2410px;width:452px;height:150px;background:var(--white);border-radius:6px;box-shadow:0 2px 5px rgba(0,0,0,.15)}
.quote-text{position:absolute;left:20px;top:22px;width:412px;font-style:italic;font-size:11.5px;line-height:22px;color:#555;text-indent:22px}
.quote-mark{position:absolute;color:#ddd;font-family:"Raleway",sans-serif;font-size:42px;font-weight:700}
.quote-name{position:absolute;left:346px;top:2574px;font-size:13px;font-weight:600;color:var(--orange)}
.post{position:absolute;left:672px;width:380px;height:60px}
.post-date{position:absolute;left:0;top:0;width:40px;height:50px;font-size:10px;text-align:center;color:var(--white)}
.post-date .d{background:#444;height:26px;line-height:26px}
.post-date .y{background:#777;height:24px;line-height:24px}
.post h4{position:absolute;left:52px;top:0;font-size:11px;font-weight:600;color:#222}
.post p{position:absolute;left:52px;top:16px;width:330px;font-size:11px;line-height:16px;color:#444}
.rule{position:absolute;left:672px;width:380px;height:1px;background:#d3d3d3}

/* Footer */
.footer{position:absolute;left:0;top:2675px;width:1200px;height:265px;background:var(--footer);color:#ddd}
.footer h5{position:absolute;font-size:13.5px;font-weight:500;color:var(--white);padding-bottom:6px;border-bottom:1px solid #555}
.links{position:absolute;left:164px;top:60px;list-style:none;font-size:12px;line-height:23px}
.links li::before{content:"›";margin-right:6px}
.contact-row{position:absolute;left:368px;font-size:12px;line-height:18px;display:flex;gap:14px}
.contact-row svg{flex:none;margin-top:2px}
.field{position:absolute;left:646px;width:166px;background:var(--white);border-radius:2px;font-size:10px;color:#444;padding:5px 6px}
.foot-brand{position:absolute;left:872px;top:76px;color:var(--orange);font-family:"Raleway",sans-serif;font-weight:700;font-size:46px;letter-spacing:1px}
.social{position:absolute;left:892px;top:184px;display:flex;gap:30px}
.social span{width:12px;height:12px;border-radius:50%;background:#ddd}
.copyright{position:absolute;left:0;top:2940px;width:1200px;height:40px;background:var(--footer-base);color:#ccc;font-size:11.5px;text-align:center;line-height:40px}
</style>
</head>
<body>

<!-- Hero -->
<section class="hero" role="img" aria-label="Photo of a business team meeting around a table with a laptop">
</section>
<aside class="sidebar">
  <div class="brand">HARLOW</div>
  <div class="brand-box"></div>
  <ul class="nav">
    <li class="active">Home</li>
    <li>About Me</li>
    <li>Event Planning Services</li>
    <li>Blog</li>
    <li>Task Force And Consulting</li>
    <li>Testimonials</li>
    <li>Contact Me</li>
  </ul>
</aside>
<svg class="abs" style="left:626px;top:186px" width="160" height="176" viewBox="0 0 160 176" aria-hidden="true">
  <path d="M44 4H6V172H44M116 4H154V172H116" fill="none" stroke="#f07a1a" stroke-width="7"/>
</svg>
<h1 class="hero-title">Event Planner And Consultant Working Independently</h1>

<!-- About -->
<h2 class="title" style="left:164px;top:616px;font-size:32px">About <span class="accent">Me</span></h2>
<div class="about-text">
  <p>Harlow Event Management specializes in event management for associations, corporations, not for profit companies and personal social events of all sizes in the mountain region.</p>
  <p>After a successful 20+ year career coordinating events in the resort community of Silverpine I am now providing her skills on the other side of the table. When you hire Harlow Event Management you are hiring a company who is intimately familiar with the inner-workings of hotels, resorts and off-site hospitality venues. You will be working with an event professional who can assist with selecting the right venue and negotiating a contract that benefits you and your company.</p>
</div>
<div class="btn" style="left:162px;top:900px;width:122px;height:40px;line-height:37px">Read More</div>
<div class="portrait-frame"><div class="portrait" role="img" aria-label="Portrait headshot of the event planner"></div></div>

<!-- Services -->
<section class="services" role="img" aria-label="Silhouettes of people in a conference room against tall windows">
  <h2 class="title" style="left:0;width:1200px;text-align:center;top:68px;font-size:32px;color:#fff">Our <span class="accent">Services</span></h2>
  <div class="service active" style="left:166px">
    <div class="ring"><div class="disc">
      <svg width="42" height="42" viewBox="0 0 42 42"><path d="M21 4L37 12 21 20 5 12Z" fill="#f07a1a"/><path d="M5 19L21 27 37 19M5 26L21 34 37 26" fill="none" stroke="#f07a1a" stroke-width="4"/></svg>
    </div></div>
    <div class="label">Site Inspections and<br>Venue Selection</div>
  </div>
  <div class="service" style="left:389px">
    <div class="ring"><div class="disc">
      <svg width="46" height="40" viewBox="0 0 46 40" fill="#333"><circle cx="15" cy="8" r="5"/><circle cx="31" cy="8" r="5"/><rect x="8" y="15" width="14" height="10" rx="3"/><rect x="24" y="15" width="14" height="10" rx="3"/><rect x="4" y="24" width="38" height="4"/><rect x="10" y="28" width="3" height="10"/><rect x="33" y="28" width="3" height="10"/></svg>
    </div></div>
    <div class="label">Contract Negotiations</div>
  </div>
  <div class="service" style="left:611px">
    <div class="ring"><div class="disc">
      <svg width="46" height="36" viewBox="0 0 46 36" fill="#333"><circle cx="23" cy="6" r="3"/><path d="M6 28A17 17 0 0 1 40 28Z"/><rect x="2" y="30" width="42" height="4" rx="1"/></svg>
    </div></div>
    <div class="label">Food and Beverage</div>
  </div>
  <div class="service" style="left:822px">
    <div class="ring"><div class="disc">
      <svg width="36" height="40" viewBox="0 0 36 40"><rect x="3" y="2" width="30" height="36" rx="3" fill="none" stroke="#333" stroke-width="3"/><rect x="8" y="7" width="20" height="7" fill="#333"/><g fill="#333"><rect x="8" y="18" width="5" height="4"/><rect x="16" y="18" width="5" height="4"/><rect x="24" y="18" width="4" height="4"/><rect x="8" y="25" width="5" height="4"/><rect x="16" y="25" width="5" height="4"/><rect x="24" y="25" width="4" height="4"/><rect x="8" y="31" width="5" height="3"/><rect x="16" y="31" width="5" height="3"/><rect x="24" y="31" width="4" height="3"/></g></svg>
    </div></div>
    <div class="label">Agenda Creation and<br>Progam Planning</div>
  </div>
</section>

<!-- Gallery -->
<h2 class="title" style="left:0;width:1200px;text-align:center;top:1602px;font-size:32px">Work <span class="accent">Gallery</span></h2>
<div class="tile" style="left:162px;top:1716px;width:432px;height:228px"><div class="ph" role="img" aria-label="Business lunch around a long table" style="background:linear-gradient(135deg,#cfd3d6,#7f8790)"></div></div>
<div class="tile" style="left:608px;top:1716px;width:208px;height:296px"><div class="ph" role="img" aria-label="Colleagues talking over a meal" style="background:linear-gradient(135deg,#d9d1c8,#5f6f8a)"></div></div>
<div class="tile" style="left:830px;top:1716px;width:214px;height:228px"><div class="ph" role="img" aria-label="Guests mingling at a reception" style="background:linear-gradient(135deg,#8a5b4a,#c9b8a8)"></div></div>
<div class="tile" style="left:162px;top:1960px;width:208px;height:236px"><div class="ph" role="img" aria-label="Attendees chatting with coffee" style="background:linear-gradient(135deg,#e4e4e4,#3e3f44)"></div></div>
<div class="tile" style="left:384px;top:1960px;width:210px;height:236px"><div class="ph" role="img" aria-label="Handshake across a table" style="background:linear-gradient(135deg,#a58c74,#5a4a3e)"></div></div>
<div class="tile" style="left:608px;top:2030px;width:208px;height:166px"><div class="ph" role="img" aria-label="Standing networking event" style="background:linear-gradient(135deg,#e7e7e4,#77746e)"></div></div>
<div class="tile" style="left:830px;top:1960px;width:214px;height:236px"><div class="ph" role="img" aria-label="Couple dining at a restaurant" style="background:linear-gradient(135deg,#6b4a35,#2e231c)"></div></div>

<!-- Testimonials & Blog -->
<section class="band"></section>
<h2 class="title" style="left:162px;top:2324px;font-size:26px">Client <span class="accent">Testimonials</span></h2>
<div class="arrows" style="left:574px;top:2346px"><span><svg width="6" height="8"><path d="M5 1L1 4 5 7" fill="none" stroke="#777" stroke-width="1.5"/></svg></span><span class="on"><svg width="6" height="8"><path d="M1 1L5 4 1 7" fill="none" stroke="#f07a1a" stroke-width="1.5"/></svg></span></div>
<div class="quote-box">
  <span class="quote-mark" style="left:16px;top:4px">“</span>
  <p class="quote-text">Lorem ipsum dolor sit amet consetug e sed diay nibh euismodl tincidunt ut laoreet dolore magam er vol wisi enim ad minim veniam quis nostrud exerci tationorem ipsum dolor sit ametee sed diammmy nibh euismd tincidunt ut laoreet dolore magna aliqur</p>
  <span class="quote-mark" style="left:242px;top:96px">”</span>
</div>
<svg class="abs" style="left:440px;top:2558px" width="50" height="24" viewBox="0 0 50 24"><path d="M0 0H50L6 22Z" fill="#fff"/></svg>
<div class="quote-name">Mr.Ellis Marlow</div>

<h2 class="title" style="left:672px;top:2324px;font-size:26px">Latest Blog <span class="accent">Posts</span></h2>
<div class="arrows" style="left:1000px;top:2346px"><span><svg width="6" height="8"><path d="M5 1L1 4 5 7" fill="none" stroke="#777" stroke-width="1.5"/></svg></span><span class="on"><svg width="6" height="8"><path d="M1 1L5 4 1 7" fill="none" stroke="#f07a1a" stroke-width="1.5"/></svg></span></div>
<div class="post" style="top:2404px"><div class="post-date"><div class="d">21 June</div><div class="y">2017</div></div><h4>Sed ut perspiciatis unde omnis iste natus error sit voluptatem</h4><p>Accusant doloremque laudantium, totamrem aperiam, eaquenm ipsa quae ab illoi facilies.</p></div>
<div class="rule" style="top:2472px"></div>
<div class="post" style="top:2482px"><div class="post-date"><div class="d">18 June</div><div class="y">2017</div></div><h4>Sed ut perspiciatis unde omnis iste natus error sit voluptatem</h4><p>Accusant doloremque laudantium, totamrem aperiam, eaquenm ipsa quae ab illoi facilies.</p></div>
<div class="rule" style="top:2548px"></div>
<div class="post" style="top:2558px"><div class="post-date"><div class="d">16 June</div><div class="y">2017</div></div><h4>Sed ut perspiciatis unde omnis iste natus error sit voluptatem</h4><p>Accusant doloremque laudantium, totamrem aperiam, eaquenm ipsa quae ab illoi facilies.</p></div>

<!-- Footer -->
<footer class="footer">
  <h5 style="left:164px;top:30px;width:170px">Quick Links</h5>
  <ul class="links">
    <li>Home</li><li>About Me</li><li>Event Planning Services</li><li>Task Force And Consulting</li><li>Testimonials</li><li>Blog</li><li>Contact Me</li>
  </ul>
  <h5 style="left:368px;top:30px;width:222px">Contact Detail</h5>
  <div class="contact-row" style="top:66px">
    <svg width="10" height="14" viewBox="0 0 10 14"><path d="M5 0A5 5 0 0 1 10 5C10 9 5 14 5 14S0 9 0 5A5 5 0 0 1 5 0Z" fill="#ddd"/><circle cx="5" cy="5" r="2" fill="#2b2b2b"/></svg>
    <div><div style="color:#fff">Harlow Event Management</div>Lorem ipsum dolor sitak amet,<br>conse.</div>
  </div>
  <div class="contact-row" style="top:132px">
    <svg width="12" height="12" viewBox="0 0 12 12"><path d="M2 0L4.5 3 3 4.5C4 6.5 5.5 8 7.5 9L9 7.5 12 10 10 12C5 12 0 7 0 2Z" fill="#ddd"/></svg>
    <div>+123 456 7890</div>
  </div>
  <div class="contact-row" style="top:158px">
    <svg width="14" height="10" viewBox="0 0 14 10"><rect width="14" height="10" rx="1" fill="#ddd"/><path d="M0 0L7 5 14 0" fill="none" stroke="#2b2b2b" stroke-width="1.2"/></svg>
    <div>info@harloweventmanagement.com</div>
  </div>
  <h5 style="left:646px;top:30px;width:180px">Quick Enquiry</h5>
  <div class="field" style="top:62px;height:26px">Name*</div>
  <div class="field" style="top:94px;height:26px">Email*</div>
  <div class="field" style="top:126px;height:56px">Message*</div>
  <div class="btn" style="left:646px;top:198px;width:92px;height:28px;line-height:25px;font-size:11px">Submit</div>
  <div class="foot-brand">HARLOW</div>
  <div class="social"><span></span><span></span><span></span><span></span></div>
</footer>
<div class="copyright">Copyright © 2017 Harlow Event Management. All Rights Reserved</div>

</body>
</html>
```